We are wanting Flagpole Technical Spec sheets custom to our company of which certain fields are editable per project to submit to architects/engineers in pdf format.
Examples 1 and 2 attached are good basic oneline details, however not very fancy and limited in details on bottom right are specific to one flagpole.
Examples 3 and 4 have better graphics however limited in details on bottom right are specific to one flagpole.
we would like a two page spec sheet. 1st page removes specifications and the second page would have flagpole specifications similar to Examples 5 and 6
page 1 editable fields would be; customer and/or job name, date, part number, notes
page 2 would like to be able to highlight, make bold, have stand out the entire line of the specific flagpole catalog number so as to show it matches the catalog number on page 1
the final design will need to include our logo attached as well as contact information at the footer as seen on examples 1 and 2

```html
<!DOCTYPE html>
<html lang="en">
<head>
<meta charset="utf-8">
<title>Aluminum Internal Rope Halyard Flagpole – Spec Sheet</title>
<link href="https://fonts.googleapis.com/css2?family=Poppins:wght@400;500;600;700&family=Oswald:wght@400;500&display=swap" rel="stylesheet">
<style>
  :root{
    --stage:#666666;
    --paper:#ffffff;
    --brand-red:#7a1316;
    --brand-gold:#a6996c;
    --gold-line:#b3a67a;
    --ink:#1f1f1f;
    --ink-soft:#4a4a4a;
    --row-alt:#ebebeb;
    --grid:#6d6d6d;
    --photo-tone:#c9ccd0;
  }
  *{box-sizing:border-box;margin:0;padding:0}
  html,body{width:1200px;height:889px;overflow:hidden;background:var(--stage)}
  body{position:relative;font-family:'Poppins',sans-serif;color:var(--ink)}
  .sheet{position:absolute;top:74px;width:525px;height:742px;background:var(--paper);box-shadow:0 2px 6px rgba(0,0,0,.35);overflow:hidden}
  .sheet--drawing{left:60px}
  .sheet--specs{left:615px}

  .sheet-title{position:absolute;font-weight:700;font-size:13.6px;letter-spacing:.1px;color:var(--ink);white-space:nowrap}
  .sheet--drawing .sheet-title{left:0;right:0;top:18px;text-align:center}
  .sheet--specs .sheet-title{left:141px;top:26px}

  .brand{position:absolute;display:flex;align-items:center;gap:5px;font-weight:700;color:var(--ink);line-height:1.05}
  .brand-mark{width:9px;height:9px;background:var(--brand-gold);flex:none}
  .sheet--drawing .brand{left:26px;top:82px;font-size:15px;width:110px}
  .sheet--specs .brand{left:50px;top:22px;font-size:11px;width:82px}

  .job-fields{position:absolute;left:140px;top:52px;width:361px}
  .job-field{display:flex;border:1px solid var(--gold-line);height:13px;margin-bottom:6px}
  .job-field--notes{height:31px;flex-direction:column;align-items:flex-start}
  .job-field label{background:var(--brand-gold);color:#fff;font-size:8.4px;line-height:12px;padding:0 4px;white-space:nowrap}
  .job-field--notes label{height:12px}

  .pole-drawing{position:absolute;left:18px;top:190px;width:134px;height:452px;background:linear-gradient(180deg,#f2f3f4 0%,#e3e6e9 70%,#b7a98a 82%,#8f8463 100%)}
  .dim-label{position:absolute;font-family:'Oswald',sans-serif;font-weight:500;font-size:11px;color:var(--ink);transform:rotate(-90deg);transform-origin:left top;white-space:nowrap}

  .callout{position:absolute;font-family:'Oswald',sans-serif;font-size:7.6px;line-height:9.6px;color:var(--ink-soft);white-space:nowrap}
  .callout strong{display:block;font-weight:500;font-size:11px;line-height:13px;color:var(--ink)}
  .callout em{font-style:normal;font-size:7.6px;color:var(--ink-soft)}
  .callout--note{white-space:normal;width:66px;border-left:1px solid var(--ink-soft);padding-left:4px}
  .callout--note b{font-weight:500;color:var(--ink)}

  .photo{position:absolute;width:76px;height:76px;border:1px solid var(--ink)}
  .photo--fill{background:radial-gradient(circle at 45% 45%,#eef0f2 0%,var(--photo-tone) 70%,#9ea3a8 100%)}
  .photo--gold{background:radial-gradient(circle at 50% 42%,#e6cf6f 0%,#b8962e 45%,#fff 46%)}

  .site-footer{position:absolute;left:0;right:0;bottom:0;height:62px}
  .footer-band{position:absolute;left:0;right:0;top:8px;height:32px;background:var(--brand-red)}
  .footer-plate{position:absolute;left:160px;width:208px;top:0;height:50px;background:var(--brand-gold);clip-path:polygon(8% 0,100% 0,92% 100%,0 100%);color:#fff;font-size:10.5px;line-height:13px;display:flex;flex-direction:column;align-items:center;justify-content:center}
  .footer-name{position:absolute;left:24px;top:10px;color:#fff;font-size:10.4px;line-height:13px}
  .footer-name b{font-weight:600;font-size:12.4px;display:block}
  .footer-contact{position:absolute;left:390px;top:12px;color:#fff;font-size:10.6px;line-height:13px;white-space:nowrap}
  .footer-contact div{display:flex;align-items:center;gap:6px}
  .footer-contact svg{width:8px;height:8px;fill:#fff}

  .spec-table{position:absolute;left:0;top:67px;width:525px;border-collapse:collapse;table-layout:fixed;font-size:8.6px}
  .spec-table th{background:var(--brand-red);color:#fff;font-weight:400;font-size:10px;line-height:11px;text-align:left;padding:3px 0 3px 5px;height:31px;vertical-align:top;border-left:1px solid rgba(255,255,255,.6)}
  .spec-table th:first-child{border-left:none}
  .spec-table th small{display:inline-block;font-size:5.2px;line-height:7px;border:1px solid #fff;padding:0 2px;margin-top:1px}
  .spec-table td{height:17.75px;text-align:center;border:1px solid var(--grid);color:var(--ink);padding:0}
  .spec-table tbody tr:nth-child(even) td{background:var(--row-alt)}
  .spec-table tbody tr:nth-child(odd) td.catalog{background:var(--brand-gold);color:#ece6d2}
</style>
</head>
<body>

<section class="sheet sheet--drawing">
  <h1 class="sheet-title">ALUMINUM INTERNAL ROPE HALYARD FLAGPOLE</h1>
  <div class="brand"><span class="brand-mark"></span>Summit Ridge Flag &amp; Flagpole</div>

  <form class="job-fields">
    <div class="job-field"><label>Customer / Job Name:</label></div>
    <div class="job-field"><label>Date:</label></div>
    <div class="job-field"><label>Part Number:</label></div>
    <div class="job-field job-field--notes"><label>Notes:</label></div>
  </form>

  <div class="pole-drawing" role="img" aria-label="Technical elevation of tapered aluminum flagpole with ground sleeve foundation section"></div>
  <span class="dim-label" style="left:24px;top:436px">Total Length</span>
  <span class="dim-label" style="left:54px;top:340px">Mounting Height</span>
  <span class="dim-label" style="left:54px;top:605px">Set Depth</span>

  <div class="callout" style="left:114px;top:172px"><strong>Truck and Ornament</strong>(see images on this sheet)</div>
  <div class="callout" style="left:21px;top:194px"><strong>Top Diameter</strong></div>
  <div class="callout" style="left:155px;top:236px">Halyard Assembly, #10<br>(5/16" Diameter)<br>Polyester Rope</div>
  <div class="callout" style="left:155px;top:278px">Two (2) Stainless Steel Swivel Flagsnaps and<br>Two (2) Neoprene Flagsnap Covers</div>
  <div class="callout" style="left:155px;top:311px">Counterweight and Retainer Ring System</div>
  <div class="callout" style="left:155px;top:367px"><strong>Wall Thickness</strong>Alloy 6063-T6 Tapered Aluminum Shaft</div>
  <div class="callout" style="left:155px;top:426px"><strong>Lock and Key</strong>Flush Access Door Continuous Piano Hinge,<br>and Manually Operated Cam Cleat</div>
  <div class="callout" style="left:155px;top:490px"><strong>Butt Diameter</strong></div>
  <div class="callout" style="left:155px;top:513px"><strong>Aluminum Collar <em>(see images on this sheet)</em></strong>Perimeter caulked by Installer</div>
  <div class="callout" style="left:155px;top:551px">2" Cap - Elastomeric sealant Compound<br>and Hardwood Wedges (By Installer)</div>
  <div class="callout" style="left:155px;top:575px">Ground Sleeve Assembly - 16 Gauge Galvanized Steel Tube</div>
  <div class="callout" style="left:155px;top:588px">Tamped Dry Sand (By Installer)</div>
  <div class="callout" style="left:155px;top:603px">3/16" Steel Plate Welded to Sleeve</div>
  <div class="callout" style="left:155px;top:615px">3/16" Steel Support Plate</div>
  <div class="callout" style="left:155px;top:627px">Lightning Spike -<br>3/4" Diameter Steel Rod</div>
  <div class="callout callout--note" style="left:273px;top:594px"><b>Note:</b> Foundation design should be completed by Structural Engineer base on site-specific Geotechnical report.</div>

  <div class="photo photo--fill" style="left:349px;top:179px" role="img" aria-label="Aluminum flagpole truck"></div>
  <div class="photo photo--gold" style="left:433px;top:179px" role="img" aria-label="Gold ball ornament"></div>
  <div class="photo photo--fill" style="left:349px;top:311px" role="img" aria-label="Aluminum flash collar"></div>
  <div class="photo" style="left:433px;top:311px;background:linear-gradient(90deg,#7d8186,#eef0f2 35%,#9da2a7 70%,#4e5257)" role="img" aria-label="Satin aluminum finish sample"></div>
  <div class="photo photo--fill" style="left:349px;top:444px" role="img" aria-label="Lock and key access door"></div>
  <div class="photo" style="left:433px;top:444px"></div>
  <div class="photo" style="left:349px;top:576px"></div>
  <div class="photo" style="left:433px;top:576px"></div>

  <footer class="site-footer">
    <div class="footer-band"></div>
    <div class="footer-name"><b>Summit Ridge</b>Flag &amp; Flagpole</div>
    <div class="footer-plate"><span>1480 Ranch Road 9</span><span>Cedar Bluff, TX 78700</span></div>
    <div class="footer-contact">
      <div><svg viewBox="0 0 10 10"><path d="M2 0l2 2.5-1 1.2c.6 1.3 1.5 2.2 2.8 2.8L7 5.5 10 7.5 8.6 10C4 9.6.4 6 0 1.4z"/></svg>512-555-0148</div>
      <div><svg viewBox="0 0 10 10"><path d="M0 2h10v6H0zM.6 2.4L5 6l4.4-3.6z" fill-rule="evenodd"/></svg>info@srflag.com</div>
    </div>
  </footer>
</section>

<section class="sheet sheet--specs">
  <div class="brand"><span class="brand-mark"></span>Summit Ridge Flag &amp; Flagpole</div>
  <h1 class="sheet-title">ALUMINUM INTERNAL ROPE HALYARD FLAGPOLE</h1>

  <table class="spec-table">
    <colgroup>
      <col style="width:34px"><col style="width:31px"><col style="width:59px"><col style="width:54px"><col style="width:43px"><col style="width:44px"><col style="width:60px"><col style="width:62px"><col style="width:39px"><col style="width:99px">
    </colgroup>
    <thead>
      <tr>
        <th>Mtg.<br>Hgt.</th><th>Butt<br>Dia.</th><th>Wall<br>Thickness</th><th>Pole<br>Sections</th><th>Set<br>Depth</th><th>Top<br>Diam.</th><th>Std. Flag<br>Size</th>
        <th colspan="2">Max Wind Speed<br><small>With Nylon Flag</small><small>No Flag</small></th>
        <th>Catalog Number<br>****Specify Finish</th>
      </tr>
    </thead>
    <tbody>
      <tr><td>20'</td><td>6"</td><td>.156"</td><td>1</td><td>2'-0"</td><td>3.5"</td><td>4' x 6'</td><td>208</td><td>301</td><td class="catalog">IRW20C61-***</td></tr>
      <tr><td></td><td>6"</td><td>.188"</td><td>1</td><td>2'-0"</td><td>3.5"</td><td>4' x 6'</td><td>229</td><td>328</td><td class="catalog">IRW20D61-***</td></tr>
      <tr><td>25'</td><td>6"</td><td>.156"</td><td>1</td><td>2'-6"</td><td>3.5"</td><td>5' x 8'</td><td>149</td><td>230</td><td class="catalog">IRW25C61-***</td></tr>
      <tr><td></td><td>6"</td><td>.188"</td><td>1</td><td>2'-6"</td><td>3.5"</td><td>5' x 8'</td><td>168</td><td>253</td><td class="catalog">IRW25D61-***</td></tr>
      <tr><td>30'</td><td>6"</td><td>.156"</td><td>1</td><td>3'-0"</td><td>3.5"</td><td>6' x 10'</td><td>108</td><td>174</td><td class="catalog">IRW30C61-***</td></tr>
      <tr><td></td><td>6"</td><td>.156"</td><td>2</td><td>3'-0"</td><td>3.5"</td><td>6' x 10'</td><td>108</td><td>174</td><td class="catalog">IRW30C62-***</td></tr>
      <tr><td></td><td>6"</td><td>.188"</td><td>1</td><td>3'-0"</td><td>3.5"</td><td>6' x 10'</td><td>122</td><td>197</td><td class="catalog">IRW30D61-***</td></tr>
      <tr><td></td><td>6"</td><td>.188"</td><td>2</td><td>3'-0"</td><td>3.5"</td><td>6' x 10'</td><td>122</td><td>197</td><td class="catalog">IRW30D62-***</td></tr>
      <tr><td></td><td>7"</td><td>.188"</td><td>1</td><td>3'-0"</td><td>3.5"</td><td>6' x 10'</td><td>157</td><td>235</td><td class="catalog">IRW30D71-***</td></tr>
      <tr><td></td><td>7"</td><td>.188"</td><td>2</td><td>3'-0"</td><td>3.5"</td><td>6' x 10'</td><td>157</td><td>235</td><td class="catalog">IRW30D72-***</td></tr>
      <tr><td>35'</td><td>6"</td><td>.156"</td><td>1</td><td>3'-6"</td><td>3.5"</td><td>6' x 10'</td><td>87</td><td>116</td><td class="catalog">IRW35C61-***</td></tr>
      <tr><td></td><td>6"</td><td>.156"</td><td>2</td><td>3'-6"</td><td>3.5"</td><td>6' x 10'</td><td>87</td><td>116</td><td class="catalog">IRW35C62-***</td></tr>
      <tr><td></td><td>6"</td><td>.188"</td><td>1</td><td>3'-6"</td><td>3.5"</td><td>6' x 10'</td><td>97</td><td>145</td><td class="catalog">IRW35D61-***</td></tr>
      <tr><td></td><td>6"</td><td>.188"</td><td>2</td><td>3'-6"</td><td>3.5"</td><td>6' x 10'</td><td>97</td><td>145</td><td class="catalog">IRW35D62-***</td></tr>
      <tr><td></td><td>6"</td><td>.156"</td><td>1</td><td>3'-6"</td><td>3.5"</td><td>6' x 10'</td><td>110</td><td>165</td><td class="catalog">IRW35C71-***</td></tr>
      <tr><td></td><td>6"</td><td>.156"</td><td>2</td><td>3'-6"</td><td>3.5"</td><td>6' x 10'</td><td>110</td><td>165</td><td class="catalog">IRW35C72-***</td></tr>
      <tr><td></td><td>7"</td><td>.188"</td><td>1</td><td>3'-6"</td><td>3.5"</td><td>6' x 10'</td><td>127</td><td>187</td><td class="catalog">IRW35D71-***</td></tr>
      <tr><td></td><td>7"</td><td>.188"</td><td>2</td><td>3'-6"</td><td>3.5"</td><td>6' x 10'</td><td>127</td><td>187</td><td class="catalog">IRW35D72-***</td></tr>
      <tr><td></td><td>7"</td><td>.188"</td><td>1</td><td>3'-6"</td><td>3.5"</td><td>6' x 10'</td><td>127</td><td>187</td><td class="catalog">IRW35D71-***</td></tr>
      <tr><td>40'</td><td>7"</td><td>.188"</td><td>2</td><td>3'-6"</td><td>3.5"</td><td>6' x 10'</td><td>127</td><td>187</td><td class="catalog">IRW35D72-***</td></tr>
      <tr><td></td><td>8"</td><td>.188"</td><td>1</td><td>3'-6"</td><td>4"</td><td>6' x 10'</td><td>155</td><td>213</td><td class="catalog">IRW35D81-***</td></tr>
      <tr><td></td><td>7"</td><td>.156"</td><td>1</td><td>4'-0"</td><td>3.5"</td><td>8' x 12'</td><td>87</td><td>122</td><td class="catalog">IRW40C71-***</td></tr>
      <tr><td></td><td>7"</td><td>.156"</td><td>2</td><td>4'-0"</td><td>3.5"</td><td>8' x 12'</td><td>87</td><td>122</td><td class="catalog">IRW40C72-***</td></tr>
      <tr><td></td><td>7"</td><td>.188"</td><td>1</td><td>4'-0"</td><td>3.5"</td><td>8' x 12'</td><td>98</td><td>147</td><td class="catalog">IRW40D71-***</td></tr>
      <tr><td></td><td>8"</td><td>.156"</td><td>1</td><td>4'-0"</td><td>4"</td><td>8' x 12'</td><td>107</td><td>157</td><td class="catalog">IRW40C81-***</td></tr>
      <tr><td></td><td>8"</td><td>.156"</td><td>2</td><td>4'-0"</td><td>3.5"</td><td>8' x 12'</td><td>107</td><td>157</td><td class="catalog">IRW40C82-***</td></tr>
      <tr><td>45'</td><td>8"</td><td>.188"</td><td>1</td><td>4'-0"</td><td>4"</td><td>8' x 12'</td><td>123</td><td>177</td><td class="catalog">IRW40D81-***</td></tr>
      <tr><td></td><td>8"</td><td>.188"</td><td>2</td><td>4'-0"</td><td>3.5"</td><td>8' x 12'</td><td>122</td><td>177</td><td class="catalog">IRW40D82-***</td></tr>
      <tr><td></td><td>8"</td><td>.188"</td><td>2</td><td>4'-0"</td><td>4"</td><td>8' x 12'</td><td>166</td><td>226</td><td class="catalog">IRW40D12-***</td></tr>
      <tr><td>50'</td><td>10"</td><td>.188"</td><td>2</td><td>4'-0"</td><td>4"</td><td>8' x 12'</td><td>102</td><td>144</td><td class="catalog">IRW45D82-***</td></tr>
      <tr><td></td><td>8"</td><td>.188"</td><td>2</td><td>4'-6"</td><td>3.5"</td><td>8' x 12'</td><td>125</td><td>173</td><td class="catalog">IRW45F82-***</td></tr>
      <tr><td></td><td>8"</td><td>.250"</td><td>2</td><td>4'-6"</td><td>3.5"</td><td>8' x 12'</td><td>143</td><td>192</td><td class="catalog">IRW45D12-***</td></tr>
    </tbody>
  </table>

  <footer class="site-footer">
    <div class="footer-band"></div>
    <div class="footer-name"><b>Summit Ridge</b>Flag &amp; Flagpole</div>
    <div class="footer-plate"><span>1480 Ranch Road 9</span><span>Cedar Bluff, TX 78700</span></div>
    <div class="footer-contact">
      <div><svg viewBox="0 0 10 10"><path d="M2 0l2 2.5-1 1.2c.6 1.3 1.5 2.2 2.8 2.8L7 5.5 10 7.5 8.6 10C4 9.6.4 6 0 1.4z"/></svg>512-555-0148</div>
      <div><svg viewBox="0 0 10 10"><path d="M0 2h10v6H0zM.6 2.4L5 6l4.4-3.6z" fill-rule="evenodd"/></svg>info@srflag.com</div>
    </div>
  </footer>
</section>

</body>
</html>
```